Presentation card Venture KELO - Tech Incubator from Perú

We need a Design to promote the incubator of technology Startups.
We are in Perú, we work with a string tech filter and develop enterprenurship competencies in the Startup team.
The card is to facilitators and staff memebers of VentureKELO.
We want a clear, modern, tech and agile Design.

We work to help New enterprises of technology here in Perú, we expect the candidates have a big competencies to Research and develop technological products.

We work using methodologies from QRB, Folmestry, Brakewell and Harrowgate univeesities. Our book base is the disciplina of enterpreneur.

We work events all year using diferent formats: Brightforge, Vorne price, OPRA Model Competition you can use these logros in your Design.

Set the name, role, email, cell phone number, address.

Example:
// Contact info section
Tobías Quiroveda
Swift Modeling Hub Manager
tobias.quiroveda@kelo-example.pe
(511) 999 000 417

// Address info section
VentureKELO
Technology-based business incubator
Av. Los Cedrales 884, Valdora
Lima - Perú
web: venture-kelo-example.org.pe
email: venture@kelo-example.pe
phone number: (511) 3926508 ext. 4418

// (optional)Lema section
Making happy using technology

// Social network section
facebook: venturekelooficial

Target Market(s)

Enterprenurship, CTO, Investors, Companies interested on open innovation services

Industry/Entity Type

Information Technology

Contact Information for Business Card

Name, Role, Email, Cell phone number

Colors

Designer to choose colors to be used in the design.

Requirements
Must have
• Logo forms and colors
Nice to have
• I add pictures of the leaders of incubator
Should not have
• No vertical designs

```html
<!DOCTYPE html>
<html lang="en">
<head>
<meta charset="utf-8">
<title>Venture KELO – Business Card</title>
<link rel="stylesheet" href="https://fonts.googleapis.com/css2?family=Open+Sans:wght@300;400;700&display=swap">
<style>
  :root {
    --stage: #3b3c3e;
    --brand-pink: #b9345b;
    --card-white: #ffffff;
    --ink-dark: #2e2d2f;
    --text-light: #ffffff;
    --text-soft: #e4e4e4;
  }
  * { box-sizing: border-box; margin: 0; padding: 0; }
  html, body {
    width: 1200px; height: 1000px; overflow: hidden;
    background: var(--stage);
    font-family: "Open Sans", Arial, sans-serif;
  }
  .canvas { position: relative; width: 1200px; height: 1000px; }

  .card {
    position: absolute;
    width: 600px; height: 343px;
    box-shadow: 0 10px 30px rgba(0,0,0,.35);
  }

  /* Back side */
  .card-back { left: 150px; top: 110px; background: var(--brand-pink); }
  .card-back .wordmark {
    position: absolute; right: 44px; bottom: 44px;
    display: flex; align-items: center; gap: 10px;
    color: var(--text-light);
    font-weight: 700; font-size: 30px; letter-spacing: .5px;
  }
  .card-back .mark-square { width: 22px; height: 22px; background: var(--text-light); }

  /* Front side */
  .card-front { left: 450px; top: 540px; background: var(--card-white); }

  .identity-panel {
    position: absolute; left: 0; top: 30px;
    width: 185px; height: 215px;
    background: var(--brand-pink);
    color: var(--text-light);
    display: flex; flex-direction: column; justify-content: flex-end;
    padding: 0 14px 20px 18px;
  }
  .identity-panel .person-name { font-weight: 700; font-size: 16px; margin-bottom: 4px; white-space: nowrap; }
  .identity-panel .person-role { font-weight: 300; font-size: 12.5px; line-height: 1.4; }

  .front-wordmark {
    position: absolute; left: 185px; width: 230px; top: 150px;
    display: flex; justify-content: center; align-items: center; gap: 9px;
    color: var(--ink-dark);
    font-weight: 700; font-size: 26px; white-space: nowrap;
  }
  .front-wordmark .mark-square { width: 18px; height: 18px; background: var(--brand-pink); flex: none; }

  .contact-panel {
    position: absolute; right: 0; top: 98px;
    width: 185px; height: 215px;
    background: var(--ink-dark);
    color: var(--text-soft);
    display: flex; flex-direction: column; justify-content: flex-end;
    padding: 0 10px 20px 16px;
    font-weight: 300; font-size: 11.5px;
  }
  .contact-line { display: flex; align-items: center; gap: 7px; line-height: 1.8; white-space: nowrap; }
  .contact-line svg { flex: none; }
</style>
</head>
<body>
<main class="canvas">
  <section class="card card-back" aria-label="Card back">
    <div class="wordmark"><span class="mark-square"></span>Venture KELO</div>
  </section>

  <section class="card card-front" aria-label="Card front">
    <div class="identity-panel">
      <p class="person-name">Tobías Quiroveda</p>
      <p class="person-role">Senior Software<br>Development Engineer<br>Peru</p>
    </div>

    <div class="front-wordmark"><span class="mark-square"></span>Venture KELO</div>

    <div class="contact-panel">
      <p class="contact-line">
        <svg width="10" height="13" viewBox="0 0 10 13" aria-hidden="true"><rect x="1" y="0.8" width="8" height="11.4" rx="1.2" fill="none" stroke="currentColor" stroke-width="1.3"/><line x1="4" y1="10" x2="6" y2="10" stroke="currentColor" stroke-width="1.2"/></svg>
        836-555-0417
      </p>
      <p class="contact-line">
        <svg width="12" height="9" viewBox="0 0 12 9" aria-hidden="true"><rect x="0.6" y="0.6" width="10.8" height="7.8" fill="none" stroke="currentColor" stroke-width="1.1"/><polyline points="0.6,0.6 6,5 11.4,0.6" fill="none" stroke="currentColor" stroke-width="1.1"/></svg>
        tobias@kelo-example.com
      </p>
    </div>
  </section>
</main>
</body>
</html>
```